Corvane Plant Services Business Card Design

Business card design

Thinking just large logo on one side with a phone number and the back side is contact info with services we offer with a industrial plant across the bottom of the card

See must haves. I will be laser etching these business cards on black metal business cards as well as full color card stock. So must be bold and professional.

Target Market(s)

Industrial manufacturing

Contact Information for Business Card

Industrial manufacturing construction business specializing in consulting project managment and completing projects turn key

Font styles to use
Other font styles liked:
• See Logo for colors and font style

Requirements
Must have
• Corvane Plant Services
• Gerald Munroe
• 2847 Alderwick Lane
• Millbrook, PA, 17402
• Project Managment
• Consulting
• Turn Key Industrial Projects
• I’d like a industrial manufacturing “cityline” on the back side bottom of the
• I’d like to be able to print these business cards in regular color on card stock but I’d also like the design to be etched into black metal business cards

```html
<!DOCTYPE html>
<html lang="en">
<head>
<meta charset="utf-8">
<title>Corvane Plant Services – Business Cards</title>
<link rel="stylesheet" href="https://fonts.googleapis.com/css2?family=Open+Sans:wght@400;600;700&display=swap">
<style>
  :root {
    --backdrop: #4a413c;
    --card-black: #141516;
    --card-edge: #1f2022;
    --brand-blue: #3f66c4;
    --text-white: #f2f2f2;
    --divider: #5a5c60;
  }
  html, body {
    margin: 0;
    padding: 0;
    width: 1200px;
    height: 864px;
    overflow: hidden;
    background: var(--backdrop);
    font-family: "Open Sans", Arial, sans-serif;
  }
  .canvas {
    position: relative;
    width: 1200px;
    height: 864px;
  }
  .card {
    position: absolute;
    width: 540px;
    height: 308px;
    background: var(--card-black);
    border: 1px solid var(--card-edge);
    border-radius: 4px;
    box-shadow: 0 10px 24px rgba(0,0,0,0.45);
    box-sizing: border-box;
  }
  /* Front card */
  .card-front { left: 50px; top: 110px; }
  .front-brand {
    position: absolute;
    left: 0; right: 0;
    top: 92px;
    display: flex;
    align-items: center;
    justify-content: center;
    gap: 14px;
  }
  .brand-square {
    width: 26px;
    height: 26px;
    background: var(--brand-blue);
  }
  .brand-name {
    color: var(--brand-blue);
    font-weight: 700;
    font-size: 30px;
    letter-spacing: 0.5px;
  }
  .front-services {
    position: absolute;
    left: 0; right: 0;
    top: 190px;
    margin: 0;
    text-align: center;
    color: var(--text-white);
    font-size: 14px;
    letter-spacing: 1.5px;
    line-height: 21px;
    text-transform: uppercase;
  }
  .front-services .dot { margin: 0 4px; }
  /* Back card */
  .card-back { left: 610px; top: 430px; }
  .back-brand {
    position: absolute;
    left: 28px;
    top: 118px;
    width: 230px;
    text-align: center;
    color: var(--brand-blue);
    font-weight: 700;
    font-size: 21px;
    line-height: 28px;
  }
  .back-divider {
    position: absolute;
    left: 278px;
    top: 40px;
    width: 1px;
    height: 228px;
    background: var(--divider);
  }
  .contact {
    position: absolute;
    left: 298px;
    top: 58px;
    color: var(--text-white);
    font-size: 13.5px;
    line-height: 20px;
  }
  .contact-name {
    color: var(--brand-blue);
    font-weight: 700;
    font-size: 17px;
    letter-spacing: 0.5px;
    text-transform: uppercase;
    margin-bottom: 12px;
  }
  .contact-address { margin-bottom: 6px; }
  .contact-row {
    display: flex;
    align-items: center;
    gap: 8px;
  }
  .contact-icon {
    width: 12px;
    height: 12px;
    flex: none;
    fill: var(--brand-blue);
  }
</style>
</head>
<body>
<main class="canvas">
  <section class="card card-front">
    <div class="front-brand">
      <span class="brand-square"></span>
      <span class="brand-name">Corvane Plant Services</span>
    </div>
    <p class="front-services">
      Project Managment<span class="dot">•</span>Consulting<br>
      Turn Key Industrial Project
    </p>
  </section>

  <section class="card card-back">
    <div class="back-brand">Corvane<br>Plant Services</div>
    <div class="back-divider"></div>
    <div class="contact">
      <div class="contact-name">Gerald Munroe</div>
      <div class="contact-address">2847 Alderwick Lane<br>Millbrook, PA, 17402</div>
      <div class="contact-row">
        <svg class="contact-icon" viewBox="0 0 12 12"><path d="M1 4c0-2 2-3 5-3s5 1 5 3l-2 1-1-2H4L3 5zM3 6h6l1 5H2z"/></svg>
        <span>717 555 0182</span>
      </div>
      <div class="contact-row">
        <svg class="contact-icon" viewBox="0 0 12 12"><path d="M3 0h6v12H3zM4 1v9h4V1z"/></svg>
        <span>717 555 0247</span>
      </div>
      <div class="contact-row">
        <svg class="contact-icon" viewBox="0 0 12 12"><path d="M3 0h5v3H3zM1 4h10v6H1zM3 10h6v2H3z"/></svg>
        <span>717 555 0369</span>
      </div>
      <div class="contact-row">
        <svg class="contact-icon" viewBox="0 0 12 12"><path d="M0 2h12v8H0zM1 3l5 4 5-4z"/></svg>
        <span>gerald@corvane.com</span>
      </div>
      <div class="contact-row">
        <svg class="contact-icon" viewBox="0 0 12 12"><circle cx="6" cy="6" r="6"/></svg>
        <span>www.corvane.com</span>
      </div>
    </div>
  </section>
</main>
</body>
</html>
```